Website icon design for ecommerce brand

I need the following icons for my website product page:
https://brindlepack.examplestore.com/pages/the-original-brindle

Guarantees etc:
- 60 Day money back guarantee
- Always free shipping (c02 neutral)
- Easy returns
- U.S. Business
- The original Brindle
- 24/7 Customer service

Product benefits:
- 40L packing volume/space
- Trolley handle sleeve
- Foldable/expandable design
- Airline carry-on compliant
- Crossbody strap
- Made to last/Durable materials
- Cross-body strap included
- Multiple smart pockets
- Wet pocket for wet items

Everything must fit the branding of the website.

```html
<!DOCTYPE html>
<html lang="en">
<head>
<meta charset="utf-8">
<title>Brindle – Guarantees &amp; Product Benefits</title>
<link href="https://fonts.googleapis.com/css2?family=Montserrat:wght@600;700&display=swap" rel="stylesheet">
<style>
  :root {
    --ink: #111111;
    --paper: #ffffff;
    --placeholder: #d6d6d6;
  }
  * { box-sizing: border-box; margin: 0; padding: 0; }
  html, body { width: 680px; height: 1200px; overflow: hidden; background: var(--paper); }
  body { font-family: "Montserrat", Arial, sans-serif; color: var(--ink); }
  .page { position: relative; width: 680px; height: 1200px; }
  .section-title {
    position: absolute; left: 0; width: 680px; text-align: center;
    font-weight: 700; font-size: 18px; letter-spacing: 0.2px; line-height: 24px;
  }
  .feature {
    position: absolute; width: 220px; margin-left: -110px;
    display: flex; flex-direction: column; align-items: center;
  }
  .feature-icon { width: 100px; height: 70px; display: block; }
  .feature-icon * { vector-effect: non-scaling-stroke; }
  .feature-label {
    margin-top: 4px; text-align: center;
    font-weight: 700; font-size: 15px; line-height: 19px;
  }
  .line { fill: none; stroke: var(--ink); stroke-width: 2.2; stroke-linecap: round; stroke-linejoin: round; }
  .solid { fill: var(--ink); }
  .glyph { font-family: "Montserrat", Arial, sans-serif; font-weight: 700; fill: var(--ink); }
  .placeholder { fill: var(--placeholder); }
</style>
</head>
<body>
<main class="page">

  <h2 class="section-title" style="top:40px">GUARANTEES</h2>

  <div class="feature" style="left:233px;top:104px">
    <svg class="feature-icon" viewBox="0 0 100 70">
      <circle class="line" cx="34" cy="42" r="14"/>
      <text class="glyph" x="34" y="49" font-size="18" text-anchor="middle">$</text>
      <path class="line" d="M44 24 A24 24 0 0 1 70 22" stroke-dasharray="1 4"/>
      <path class="line" d="M70 22 A20 20 0 0 1 54 60"/>
      <path class="solid" d="M50 60 l8 -5 l0 10 z"/>
      <text class="glyph" x="58" y="38" font-size="11" text-anchor="middle" font-weight="600">60</text>
    </svg>
    <p class="feature-label">60-Day money back<br>guarantee</p>
  </div>

  <div class="feature" style="left:437px;top:104px">
    <svg class="feature-icon" viewBox="0 0 100 70">
      <path class="line" d="M22 22 H40 M16 30 H36 M24 38 H34 M28 46 H36"/>
      <path class="line" d="M40 17 H72 V52 H34 M72 32 H82 L90 42 V52 H86"/>
      <circle class="line" cx="40" cy="54" r="6"/>
      <circle class="line" cx="78" cy="54" r="6"/>
      <path class="line" d="M52 42 C50 32 56 24 66 23 C67 33 61 40 52 42 Z M52 42 L60 30"/>
    </svg>
    <p class="feature-label">Always free shipping<br>(c02 neutral)</p>
  </div>

  <div class="feature" style="left:233px;top:234px">
    <svg class="feature-icon" viewBox="0 0 100 70">
      <path class="line" d="M42 8 A22 22 0 1 1 54 54"/>
      <path class="solid" d="M48 56 l9 -6 l0 11 z"/>
      <path class="line" d="M16 36 L28 29 L40 36 L40 50 L28 57 L16 50 Z M16 36 L28 43 L40 36 M28 43 V57"/>
    </svg>
    <p class="feature-label">Easy returns</p>
  </div>

  <div class="feature" style="left:437px;top:234px">
    <svg class="feature-icon" viewBox="0 0 100 70">
      <rect class="placeholder" x="40" y="18" width="48" height="44" rx="6" role="img" aria-label="Outline map of the United States"/>
      <circle class="line" cx="36" cy="22" r="14" style="fill:#fff"/>
      <text class="glyph" x="36" y="29" font-size="18" text-anchor="middle">$</text>
    </svg>
    <p class="feature-label">U.S. Business</p>
  </div>

  <div class="feature" style="left:233px;top:344px">
    <svg class="feature-icon" viewBox="0 0 100 70">
      <circle class="line" cx="48" cy="39" r="26"/>
      <path class="line" d="M34 40 L44 52 L78 24"/>
      <circle class="line" cx="50" cy="26" r="4.5" style="stroke-width:1.4"/>
      <text class="glyph" x="50" y="28.6" font-size="6" text-anchor="middle">R</text>
    </svg>
    <p class="feature-label">The original Brindle</p>
  </div>

  <div class="feature" style="left:437px;top:344px">
    <svg class="feature-icon" viewBox="0 0 100 70">
      <path class="line" d="M32 28 A26 26 0 1 1 72 62"/>
      <circle class="solid" cx="74" cy="60" r="3.5"/>
      <path class="line" d="M34 26 A22 22 0 1 1 38 50 L30 62 L31 48 A22 22 0 0 1 34 26"/>
      <path class="line" d="M28 42 A6 6 0 0 0 30 52"/>
      <path class="solid" d="M56 52 l8 -5 l0 10 z"/>
      <text class="glyph" x="53" y="42" font-size="12" text-anchor="middle" font-weight="600">24/7</text>
    </svg>
    <p class="feature-label">24/7 Customer service</p>
  </div>

  <h2 class="section-title" style="top:529px">PRODUCT BENEFITS</h2>

  <div class="feature" style="left:230px;top:591px">
    <svg class="feature-icon" viewBox="0 0 100 70">
      <path class="line" d="M20 8 L30 24 H80 L90 8 M30 24 V66 H80 V24"/>
      <path class="line" d="M38 4 V18 M72 4 V18"/>
      <path class="solid" d="M35 16 h6 l-3 5 z M69 16 h6 l-3 5 z"/>
      <path class="line" d="M52 38 H74 M52 45 H74 M52 52 H74 M36 59 H74"/>
      <text class="glyph" x="40" y="50" font-size="11" text-anchor="middle" font-weight="600">40</text>
    </svg>
    <p class="feature-label">40L packing<br>volume/space</p>
  </div>

  <div class="feature" style="left:441px;top:591px">
    <svg class="feature-icon" viewBox="0 0 100 70">
      <rect class="line" x="38" y="0" width="22" height="44" rx="3"/>
      <path class="line" d="M20 68 V54 Q20 44 30 44 H68 Q78 44 78 54 V68"/>
      <path class="line" d="M49 28 V14"/>
      <path class="solid" d="M46 15 l3 -5 l3 5 z"/>
    </svg>
    <p class="feature-label">Trolley handle sleeve</p>
  </div>

  <div class="feature" style="left:230px;top:725px">
    <svg class="feature-icon" viewBox="0 0 100 70">
      <rect class="line" x="14" y="2" width="56" height="64" stroke-dasharray="5 4"/>
      <rect class="line" x="50" y="14" width="28" height="52" style="fill:#fff"/>
      <rect class="line" x="38" y="2" width="28" height="50" style="fill:#fff"/>
      <path class="solid" d="M66 52 L50 66 V52 Z"/>
      <path class="line" d="M30 48 L20 58 M20 50 V58 H28"/>
    </svg>
    <p class="feature-label">Foldable/expandable<br>design</p>
  </div>

  <div class="feature" style="left:441px;top:725px">
    <svg class="feature-icon" viewBox="0 0 100 70">
      <path class="line" d="M34 16 V6 H46 M26 16 H42 Q48 16 48 22 M26 16 Q18 16 18 24 V58 Q18 64 24 64 H56"/>
      <path class="line" d="M28 24 V58 M30 70 A3 3 0 0 0 30 64"/>
      <circle class="line" cx="72" cy="14" r="10"/>
      <path class="line" d="M66 14 L71 19 L80 8"/>
      <path class="line" d="M40 48 H60 L78 34 Q84 32 82 38 L66 50 L72 62 H66 L58 52 H44 Z M54 42 L46 34 H52 L62 42"/>
    </svg>
    <p class="feature-label">Airline carry-on<br>compliant</p>
  </div>

  <div class="feature" style="left:230px;top:873px">
    <svg class="feature-icon" viewBox="0 0 100 70">
      <rect class="placeholder" x="30" y="0" width="40" height="70" rx="14" role="img" aria-label="Figure wearing a bag strap across the body"/>
    </svg>
    <p class="feature-label">Crossbody strap</p>
  </div>

  <div class="feature" style="left:441px;top:873px">
    <svg class="feature-icon" viewBox="0 0 100 70">
      <path class="line" d="M50 0 L82 12 V34 Q82 58 50 70 Q18 58 18 34 V12 Z"/>
      <circle class="line" cx="50" cy="34" r="14"/>
      <path class="line" d="M43 34 L48 39 L60 28"/>
    </svg>
    <p class="feature-label">Made to last/Durable<br>materials</p>
  </div>

  <div class="feature" style="left:230px;top:1014px">
    <svg class="feature-icon" viewBox="0 0 100 70">
      <path class="line" d="M10 32 H36 V52 Q36 62 23 62 Q10 62 10 52 Z"/>
      <path class="line" d="M40 20 H66 V40 Q66 50 53 50 Q40 50 40 40 Z"/>
      <path class="line" d="M70 32 H96 V52 Q96 62 83 62 Q70 62 70 52 Z"/>
    </svg>
    <p class="feature-label">Multiple smart<br>pockets</p>
  </div>

  <div class="feature" style="left:441px;top:1014px">
    <svg class="feature-icon" viewBox="0 0 100 70">
      <path class="line" d="M28 2 H72 V46 Q72 68 50 68 Q28 68 28 46 Z"/>
      <path class="line" d="M50 18 Q40 32 40 38 A10 10 0 0 0 60 38 Q60 32 50 18 Z"/>
    </svg>
    <p class="feature-label">Wet pocket<br>for wet items</p>
  </div>

</main>
</body>
</html>
```